Window Cleaning Flyer targeting Shopfronts and Small Commercial Work

Single page flyer similar to the flyer targeting small commercial work and shopfronts

Please include the following text:

Brisk Pane Services delivers high quality service to suburbs all around Melbourne. From Frankston to Kalkallo, Brisk has you covered!

With over 10 years experience, Brisk specialises in providing:
- Window Cleaning: via elevated work platforms, rope access and extension poles
- Pressure Cleaning: Including chlorine treatment to prevent mould regrowth on concrete area
- Roof Gutter Cleaning: using our ladder free gutter vacuum

We pride ourselves on neat and professional presentation and vast geographical reach across Melbourne.

Our services can be completed on a frequency that meets your window cleaning needs. Whether a weekly clean or a yearly service.

Brisk Pane Services Melbourne takes care of all your window cleaning needs.

Contact Us now for free quote!

Target Market(s)

Small business and commercial building owners

Industry/Entity Type

Window Cleaning

Requirements
Must have
• Only use photos/logos provided
Should not have
• Stock phots

```html
<!DOCTYPE html>
<html lang="en">
<head>
<meta charset="utf-8">
<title>Brisk Pane Services – Flyer</title>
<link rel="stylesheet" href="https://fonts.googleapis.com/css2?family=Roboto:wght@300;400;700&family=Archivo+Black&display=swap">
<style>
  :root {
    --navy: #0d4f80;
    --yellow: #fcee1f;
    --paper: #ececec;
    --grey-text: #8a8a8a;
    --white: #ffffff;
  }
  * { margin: 0; padding: 0; box-sizing: border-box; }
  html, body { width: 928px; height: 1200px; overflow: hidden; }
  body {
    font-family: "Roboto", Arial, sans-serif;
    background: radial-gradient(ellipse at 30% 20%, #f6f6f6 0%, var(--paper) 60%, #e2e2e2 100%);
    position: relative;
  }
  .flyer { position: relative; width: 928px; height: 1200px; }
  .abs { position: absolute; }

  .headline { left: 29px; top: 48px; color: var(--navy); line-height: 1; }
  .headline .line-bold { font-weight: 700; font-size: 34px; letter-spacing: 0.3px; }
  .headline .line-light { font-weight: 400; font-size: 30px; margin-top: 3px; }
  .intro {
    left: 29px; top: 127px; width: 335px;
    color: var(--grey-text); font-weight: 300; font-size: 17.5px; line-height: 22px;
    text-transform: uppercase;
  }

  .brand { left: 706px; top: 38px; width: 196px; text-align: right; color: var(--navy);
    font-weight: 700; line-height: 1; }
  .brand .brand-main { font-size: 50px; letter-spacing: 1px; }
  .brand .brand-sub { font-size: 16px; margin-top: 6px; letter-spacing: 0.4px; }

  .bar { background: var(--navy); }
  .photo { display: block; }

  .callout { left: 0; top: 728px; width: 422px; height: 198px; background: var(--yellow);
    padding: 22px 0 0 28px; color: var(--navy); }
  .callout p { font-weight: 300; font-size: 33px; line-height: 37px; }
  .callout .covered { font-family: "Archivo Black", "Roboto", sans-serif; font-size: 38px; line-height: 44px; }

  .info-panel { left: 0; top: 948px; width: 928px; height: 252px; background: var(--navy); color: var(--white); }
  .services { left: 29px; top: 20px; width: 375px; }
  .services h2 { font-weight: 400; font-size: 18px; line-height: 23px; }
  .services h2 strong { font-weight: 700; }
  .services ul { list-style: none; margin-top: 14px; }
  .services li { position: relative; padding-left: 21px; font-size: 14.5px; line-height: 18.5px; font-weight: 300; margin-bottom: 9px; }
  .services li strong { font-weight: 400; }
  .services li svg { position: absolute; left: 0; top: 3px; }
  .about { left: 454px; top: 20px; width: 450px; font-size: 14.5px; line-height: 18.5px; font-weight: 300; }
  .about p { margin-bottom: 8px; }
  .about .about-strong { font-weight: 400; }
  .contact { left: 454px; top: 174px; width: 452px; color: var(--white); }
  .contact .cta { font-size: 18.5px; font-weight: 400; white-space: nowrap; }
  .contact .cta strong { color: var(--yellow); font-weight: 700; }
  .contact .lines { margin-top: 5px; display: flex; align-items: center; gap: 6px; white-space: nowrap;
    font-family: "Archivo Black", "Roboto", sans-serif; font-size: 16px; color: var(--yellow); letter-spacing: 0.3px; }
  .contact .lines span { white-space: nowrap; }
  .contact .sep { color: var(--white); font-family: "Roboto", sans-serif; font-weight: 700; font-style: italic; margin: 0 8px; }
</style>
</head>
<body>
<main class="flyer">
  <header class="headline abs">
    <div class="line-bold">BRISK PANE</div>
    <div class="line-light">SERVICES DELIVERS</div>
  </header>
  <p class="intro abs">High quality service to suburbs all around Melbourne. From Frankston to Kalkallo, Brisk has you covered!</p>

  <div class="brand abs">
    <div class="brand-main">BRISK</div>
    <div class="brand-sub">PANE SERVICES</div>
  </div>

  <div class="bar abs" style="left:0;top:227px;width:365px;height:27px;"></div>

  <svg class="photo abs" style="left:0;top:284px;" width="422" height="364" role="img" aria-label="Photo of a technician cleaning windows of a timber-slatted commercial building with an extension pole">
    <defs><linearGradient id="g1" x1="0" y1="0" x2="1" y2="1"><stop offset="0" stop-color="#b58a57"/><stop offset="0.7" stop-color="#8a7a6c"/><stop offset="1" stop-color="#6f7a52"/></linearGradient></defs>
    <rect width="422" height="364" fill="url(#g1)"/>
  </svg>

  <div class="bar abs" style="left:454px;top:146px;width:474px;height:28px;"></div>
  <div class="bar abs" style="left:454px;top:146px;width:27px;height:254px;"></div>
  <svg class="photo abs" style="left:506px;top:200px;" width="422" height="272" role="img" aria-label="Black and white photo of a technician on an elevated work platform cleaning upper-storey windows">
    <defs><linearGradient id="g2" x1="0" y1="0" x2="1" y2="0"><stop offset="0" stop-color="#7d7d7d"/><stop offset="0.5" stop-color="#4a4a4a"/><stop offset="1" stop-color="#c8c8c8"/></linearGradient></defs>
    <rect width="422" height="272" fill="url(#g2)"/>
  </svg>

  <div class="bar abs" style="left:454px;top:496px;width:474px;height:27px;"></div>
  <svg class="photo abs" style="left:506px;top:556px;" width="422" height="370" role="img" aria-label="Photo of a technician using a water-fed pole to clean windows on a two-storey brick house with a balcony">
    <defs><linearGradient id="g3" x1="0" y1="0" x2="0" y2="1"><stop offset="0" stop-color="#6e5a48"/><stop offset="0.45" stop-color="#3f6e68"/><stop offset="1" stop-color="#8a5a3e"/></linearGradient></defs>
    <rect width="422" height="370" fill="url(#g3)"/>
  </svg>

  <div class="bar abs" style="left:100px;top:674px;width:378px;height:28px;"></div>
  <div class="bar abs" style="left:451px;top:674px;width:27px;height:274px;"></div>

  <section class="callout abs">
    <p>FROM FRANKSTON<br>TO KALKALLO, BRISK<br>HAS YOU</p>
    <p class="covered">COVERED!</p>
  </section>

  <section class="info-panel abs">
    <div class="services abs">
      <h2>With over <strong>10 years experience</strong><br>Brisk specialises in providing:</h2>
      <ul>
        <li><svg width="14" height="12" viewBox="0 0 14 12"><path d="M1 7 L5 11 L13 1" fill="none" stroke="#fcee1f" stroke-width="2.4"/></svg><strong>Window Cleaning:</strong> via elevated work platforms, rope access and extension poles</li>
        <li><svg width="14" height="12" viewBox="0 0 14 12"><path d="M1 7 L5 11 L13 1" fill="none" stroke="#fcee1f" stroke-width="2.4"/></svg><strong>Pressure Cleaning:</strong> Including chlorine treatment to prevent mould regrowth on concrete area</li>
        <li><svg width="14" height="12" viewBox="0 0 14 12"><path d="M1 7 L5 11 L13 1" fill="none" stroke="#fcee1f" stroke-width="2.4"/></svg><strong>Roof Gutter Cleaning:</strong> using our ladder free gutter vacuum</li>
      </ul>
    </div>
    <div class="about abs">
      <p>We pride ourselves on neat and professional presentation and vast geographical reach across Melbourne.</p>
      <p>Our services can be completed on a frequency that meets your window cleaning needs. Whether a weekly clean or a yearly service.</p>
      <p class="about-strong">Brisk Pane Services Melbourne takes care of all your window cleaning needs.</p>
    </div>
    <div class="contact abs">
      <div class="cta"><strong>CONTACT US</strong> now for <strong>FREE QUOTE!</strong></div>
      <div class="lines">
        <svg width="10" height="16" viewBox="0 0 10 16"><rect x="1" y="1" width="8" height="14" rx="1.5" fill="none" stroke="#ffffff" stroke-width="1.6"/><rect x="3" y="3.5" width="4" height="6" fill="#ffffff"/></svg>
        <span>0491 570 110</span>
        <span class="sep">//</span>
        <svg width="12" height="12" viewBox="0 0 12 12"><circle cx="6" cy="6" r="5" fill="none" stroke="#ffffff" stroke-width="1.3"/><path d="M1 6 H11 M6 1 V11" stroke="#ffffff" stroke-width="1"/></svg>
        <span>www.briskpane.example</span>
      </div>
    </div>
  </section>
</main>
</body>
</html>
```